Progressive/contemporary business card design for successful Startups as a Service Company

New logo launched in 2020. New website launched in 2021. Now that COVID is (mostly) behind us, I'm networking with more people and need a business card that matches the company/logo design aesthetic.

```html
<!DOCTYPE html>
<html lang="en">
<head>
<meta charset="utf-8">
<title>Launchwell Business Card</title>
<link href="https://fonts.googleapis.com/css2?family=Arimo:wght@400;700&display=swap" rel="stylesheet">
<style>
  :root {
    --page-bg: #0e0e0e;
    --card-bg: #1d1d1d;
    --card-edge: #262626;
    --ink-light: #f2f2f2;
    --ink-muted: #cfcfcf;
    --accent: #f5b50a;
    --mark-tone-a: #2a2a2a;
    --mark-tone-b: #1f1f1f;
    --pattern-a: #242424;
    --pattern-b: #3a3a3a;
  }
  * { box-sizing: border-box; margin: 0; padding: 0; }
  html, body {
    width: 1200px; height: 963px; overflow: hidden;
    background: var(--page-bg);
    font-family: "Arimo", Arial, sans-serif;
  }
  .sheet {
    width: 1200px; height: 963px;
    display: flex; flex-direction: column;
    align-items: center; justify-content: center; gap: 60px;
  }
  .card {
    position: relative;
    width: 700px; height: 400px;
    background: var(--card-bg);
    border: 1px solid var(--card-edge);
    box-shadow: 0 18px 40px rgba(0,0,0,.6);
    overflow: hidden;
  }
  /* Front */
  .front__mark-area {
    position: absolute; right: 0; top: 60px;
    width: 330px; height: 340px;
    background: linear-gradient(135deg, var(--mark-tone-b) 0%, var(--mark-tone-a) 55%, var(--mark-tone-b) 100%);
    opacity: .7;
  }
  .wordmark {
    position: absolute; left: 230px; top: 62px;
    font-size: 40px; font-weight: 400;
    letter-spacing: 9px; color: var(--ink-light);
    text-transform: uppercase;
  }
  .identity { position: absolute; left: 60px; top: 168px; }
  .identity__name {
    font-size: 25px; font-weight: 700; color: var(--accent);
    text-transform: uppercase; letter-spacing: .5px;
  }
  .identity__role { font-size: 19px; color: var(--ink-light); margin-top: 2px; }
  .contacts { position: absolute; left: 40px; top: 252px; list-style: none; }
  .contacts__item {
    display: flex; align-items: center; gap: 12px;
    font-size: 19px; color: var(--ink-light); line-height: 28px;
  }
  .contacts__icon { width: 18px; height: 18px; fill: var(--accent); flex: none; }
  .address {
    position: absolute; right: 40px; bottom: 40px;
    font-size: 19px; line-height: 25px; color: var(--ink-light); text-align: left;
  }
  /* Back */
  .back__pattern {
    position: absolute; inset: 0;
    background: linear-gradient(135deg, var(--pattern-a) 0%, var(--pattern-b) 50%, var(--pattern-a) 100%);
  }
  .back__wordmark {
    position: absolute; left: 0; right: 0; top: 50%;
    transform: translateY(-50%);
    text-align: center;
    font-size: 40px; font-weight: 400; letter-spacing: 9px;
    color: var(--ink-light); text-transform: uppercase;
  }
</style>
</head>
<body>
<main class="sheet">
  <section class="card card--front" aria-label="Business card front">
    <div class="front__mark-area" role="img" aria-label="Faint large brand mark decoration"></div>
    <div class="wordmark">Launchwell</div>
    <div class="identity">
      <p class="identity__name">Marcus Hale</p>
      <p class="identity__role">Manager</p>
    </div>
    <ul class="contacts">
      <li class="contacts__item">
        <svg class="contacts__icon" viewBox="0 0 24 24" aria-hidden="true"><path d="M6.6 10.8a15.2 15.2 0 0 0 6.6 6.6l2.2-2.2a1 1 0 0 1 1-.25 11.4 11.4 0 0 0 3.6.57 1 1 0 0 1 1 1V20a1 1 0 0 1-1 1A17 17 0 0 1 3 4a1 1 0 0 1 1-1h3.5a1 1 0 0 1 1 1c0 1.25.2 2.46.57 3.6a1 1 0 0 1-.25 1z"/></svg>
        <span>555-014-2100</span>
      </li>
      <li class="contacts__item">
        <svg class="contacts__icon" viewBox="0 0 24 24" aria-hidden="true"><path d="M2 5h20v14H2z M3 6l9 7 9-7" fill="none" stroke="var(--accent)" stroke-width="0"/><path d="M2 5h20v2l-10 7L2 7z"/><path d="M2 9l10 7 10-7v10H2z"/></svg>
        <span>hello@launchwell.co</span>
      </li>
      <li class="contacts__item">
        <svg class="contacts__icon" viewBox="0 0 24 24" aria-hidden="true"><circle cx="12" cy="12" r="10" fill="none" stroke="var(--accent)" stroke-width="2.2"/><path d="M2 12h20M12 2c3 3 3 17 0 20M12 2c-3 3-3 17 0 20" fill="none" stroke="var(--accent)" stroke-width="1.8"/></svg>
        <span>www.launchwell.co</span>
      </li>
    </ul>
    <p class="address">Your address, city<br>state, ZIP 0000</p>
  </section>

  <section class="card card--back" aria-label="Business card back">
    <div class="back__pattern" role="img" aria-label="Embossed geometric triangle pattern"></div>
    <div class="back__wordmark">Launchwell</div>
  </section>
</main>
</body>
</html>
```